Real Estate 24"x24" Sign, Business Card, Letter Head and Envelope

This is a 4 project contest. If we choose a design or designs we like from what you sent we are willing to pay an amount at our discretion for that design even if we don't like all your designs for the 4 projects. Please be creative. Attached are our logo files. Please message us with any questions. Thanks and Good Luck!
Project 1: QMTD Realty 24" x 24" yard sign
We want to use the same blue background in our logo for the sign where the logo in white font will be on. CMYK 100,80,0,0. Attached is a sample a local designer made for you to get an idea what we are looking for. In the sample, the website is way too big and the entire sign is very plain and not attractive looking plus blue color is wrong one. We want the logo on top as large as possible but keeping it proportionate and attractive looking buy not too big that it looks odd. The following information can go in white color background or same blue color background color. Our company colors are blue (as per logo), green (as per logo), and white. "Residential & Commercial" goes under the logo. Under that put our phone number "312-640-5918" as large as possible but still looks good and under that our website in much smaller but readable font "www.qmtdrealty.com".
Project 2: Envelope
We have two version of the logo. Use one or both. Whatever looks best in your design. The envelope will be white. We only want on top left corner logo and underneath our mailing address: 5147 Hawthorne Ave. Elmridge, NY 60091-2714. Maybe some creative decorative design at bottom of envelope will look nice
Project 3: Letter Head
We have two version of the logo. Use one or both. Whatever looks best in your design. We want the following information on the top of the letterhead. Logo, address: 5147 Hawthorne Ave., Elmridge, NY 60091-2714, phone: 312-640-5918, fax: 312-918-6057 website www.qmtdrealty.com, email: info@qmtdrealty.com
Project 4: Business card
Use either logo. We need cards for two individuals. Information for Person 1: Dev Mehta, Managing Broker, Phone: 312-640-5918, Email: dev.mehta@qmtdrealty.com. Person 2: Raj Mehta Broker Phone: 312-285-3390 Email: raj.mehta@qmtdrealty.com. Add Address, Fax and website same as above letter head.

```html
<!DOCTYPE html>
<html lang="en">
<head>
<meta charset="utf-8">
<title>QMTD Realty Letterhead</title>
<link rel="stylesheet" href="https://fonts.googleapis.com/css2?family=Questrial&display=swap">
<style>
  :root {
    --brand-blue: #1d4fa3;
    --brand-green: #6cbb3c;
    --ink: #4d4d4d;
    --ink-soft: #666666;
    --rule: #9a9a9a;
    --paper: #f8f8f8;
    --backdrop: #e4e4e4;
    --ghost: #eceef2;
  }
  * { margin: 0; padding: 0; box-sizing: border-box; }
  html, body {
    width: 882px; height: 1200px; overflow: hidden;
    background: var(--backdrop);
    font-family: "Questrial", "Century Gothic", sans-serif;
    color: var(--ink);
  }
  .sheet {
    position: absolute; left: 41px; top: 36px;
    width: 801px; height: 1129px;
    background: linear-gradient(90deg, #ffffff 0%, var(--paper) 100%);
    box-shadow: 0 2px 10px rgba(0,0,0,0.18);
    overflow: hidden;
  }
  .brand {
    position: absolute; left: 62px; top: 92px;
    display: flex; align-items: center; gap: 10px;
  }
  .brand-mark { width: 20px; height: 20px; background: var(--brand-blue); }
  .brand-name { font-size: 26px; color: var(--brand-blue); letter-spacing: 0.5px; white-space: nowrap; }
  .contact { position: absolute; top: 125px; font-size: 11.5px; line-height: 16px; color: var(--ink); font-style: normal; }
  .contact-address { left: 255px; }
  .contact-phones { left: 444px; }
  .contact-web { left: 606px; }
  .contact-row { display: flex; align-items: center; gap: 8px; }
  .contact-row svg { width: 10px; height: 10px; fill: var(--brand-blue); flex: none; }
  .header-rule {
    position: absolute; left: 69px; top: 175px; width: 667px;
    height: 1px; background: var(--rule);
  }
  .letter { position: absolute; left: 69px; top: 314px; width: 667px; }
  .salutation { font-size: 22px; line-height: 28px; font-weight: normal; color: var(--ink); margin-bottom: 34px; }
  .letter p {
    font-size: 11px; line-height: 14.8px; color: var(--ink-soft);
    text-align: justify; margin-bottom: 24px;
  }
  .closing { margin-top: 30px; font-size: 11px; color: var(--ink-soft); }
  .signature {
    margin-top: 24px; width: 150px; height: 60px;
    background: linear-gradient(90deg, rgba(29,79,163,0.10), rgba(29,79,163,0.04));
    border-radius: 4px;
  }
  .footer-glow {
    position: absolute; left: 0; bottom: 14px; width: 100%; height: 200px;
    background: linear-gradient(180deg, rgba(236,238,242,0) 0%, var(--ghost) 100%);
  }
  .footer-band { position: absolute; left: 0; bottom: 0; width: 801px; height: 14px; }
</style>
</head>
<body>
  <main class="sheet">
    <header>
      <div class="brand">
        <span class="brand-mark"></span>
        <span class="brand-name">QMTD Realty</span>
      </div>
      <address class="contact contact-address">
        5147 Hawthorne Ave.<br>Elmridge, NY 60091-2714
      </address>
      <div class="contact contact-phones">
        <div class="contact-row">
          <svg viewBox="0 0 10 10"><path d="M2 0.5 L3.6 0.5 L4.2 2.8 L3 3.7 Q4 6 6.3 7 L7.2 5.8 L9.5 6.4 L9.5 8 Q9.5 9.5 8 9.5 Q0.5 9 0.5 2 Q0.5 0.5 2 0.5Z"/></svg>
          <span>312-640-5918</span>
        </div>
        <div class="contact-row">
          <svg viewBox="0 0 10 10"><rect x="2.5" y="0.5" width="5" height="3"/><rect x="0.5" y="3.5" width="9" height="4" rx="1"/><rect x="2.5" y="6.5" width="5" height="3"/></svg>
          <span>312-918-6057</span>
        </div>
      </div>
      <div class="contact contact-web">
        <div class="contact-row">
          <svg viewBox="0 0 10 10"><rect x="0.5" y="2" width="9" height="6.5" rx="0.8"/><path d="M0.8 2.4 L5 5.6 L9.2 2.4" stroke="#fff" stroke-width="0.9" fill="none"/></svg>
          <span>info@qmtdrealty.com</span>
        </div>
        <div class="contact-row">
          <svg viewBox="0 0 10 10"><circle cx="5" cy="5" r="4.5"/><path d="M0.8 5 H9.2 M5 0.6 Q2.5 5 5 9.4 M5 0.6 Q7.5 5 5 9.4" stroke="#fff" stroke-width="0.7" fill="none"/></svg>
          <span>www.qmtdrealty.com</span>
        </div>
      </div>
      <div class="header-rule"></div>
    </header>

    <article class="letter">
      <h1 class="salutation">Dear Mr. Carter,</h1>
      <p>Lorem ipsum dolor sit amet, consectetur adipiscing elit. Donec orci purus, luctus vitae dignissim eu, iaculis sed purus. Vivamus faucibus, ipsum nec aliquet viverra, leo mauris condimentum ligula, sit amet sagittis enim ligula quis arcu. Nam egestas tortor id nisi porttitor mattis. In tortor ante, ultricies in suscipit a, tempus non massa. Vivamus et auctor mi. Fusce vel massa nulla. Phasellus nec eros mauris, et scelerisque orci.</p>
      <p>Donec malesuada orci vitae nulla accumsan porta a id massa. Quisque accumsan iaculis magna sit amet fringilla. Maecenas consequat, magna eget tincidunt semper, odio nibh rutrum mi, id feugiat ante nisi eu risus. Vestibulum nunc orci, rhoncus a placerat in, ultricies in mi. Cras mattis varius eros, vel fringilla nisi suscipit eget. Quisque scelerisque sagittis nulla at porttitor.</p>
      <p>Sed id augue vitae urna euismod commodo aliquet a quam. Pellentesque arcu velit, cursus et malesuada ut, consequat et diam. Nullam erat sem, rhoncus id ullamcorper vitae, rhoncus et arcu. In ultricies ultricies nulla, ut rutrum nisi iaculis at. Donec eu magna a metus ornare faucibus. Fusce aliquet faucibus ultricies. Morbi semper, est id tincidunt gravida, sem arcu adipiscing lacus, ac bibendum nulla leo eu purus. Quisque nec diam sed risus consectetur accumsan quis quis nibh. Vestibulum id purus lorem.</p>
      <p>It is a long established fact that a reader will be distracted by the readable content of a page when looking at its layout. The point of using Lorem Ipsum is that it has a more-or-less normal distribution of letters, as opposed to using 'Content here, content here', making it look like readable English. Many desktop publishing packages</p>
      <div class="closing">Sincerely,</div>
      <div class="signature" role="img" aria-label="Handwritten signature of Paul Carter"></div>
    </article>

    <div class="footer-glow"></div>
    <svg class="footer-band" viewBox="0 0 801 14" preserveAspectRatio="none">
      <polygon points="0,0 408,0 396,14 0,14" fill="var(--brand-blue)"/>
      <polygon points="410,0 801,0 801,14 398,14" fill="var(--brand-green)"/>
    </svg>
  </main>
</body>
</html>
```